Behavioral Health Booth Backdrop Design

I need a design created for our backdrop as we are purchasing a new curved 10x10 backdrop for our trade shows. We are a behavioral health (mental health and addiction services) agency and want something that catches your eye when walking by. We don't want a lot of "words" or description on it, but more of a catchy look. I have attached some pics that we like the colors of in general (abstract). This doesn't mean that you need to use these specific pics. I have also attached our Logo with our name.

• Eye catchy design and or a picture/photo with our agency name and/or logo on the backdrop. One of the files to be a vector file.

```html
<!DOCTYPE html>
<html lang="en">
<head>
<meta charset="utf-8">
<title>Maple Hollow – Promoting Wellness and Recovery</title>
<link rel="stylesheet" href="https://fonts.googleapis.com/css2?family=Roboto:wght@400;500;700&family=Montserrat:wght@800&display=swap">
<style>
  :root {
    --blue: #2a8cc4;
    --green: #3a8a1e;
    --tick: #5fd02a;
    --ink: #111111;
    --white: #ffffff;
  }
  * { margin: 0; padding: 0; box-sizing: border-box; }
  html, body { width: 1200px; height: 1200px; overflow: hidden; background: var(--white); }
  .backdrop { position: relative; width: 1200px; height: 1200px; overflow: hidden; font-family: "Roboto", Arial, sans-serif; }
  .backdrop-art { position: absolute; inset: 0; }

  .brand { position: absolute; top: 62px; left: 0; width: 1200px; display: flex; justify-content: center; align-items: center; gap: 18px; }
  .brand-dot { width: 74px; height: 74px; border-radius: 50%; background: var(--green); }
  .brand-name { font-weight: 400; font-size: 56px; letter-spacing: 1px; color: var(--ink); }

  .headline { position: absolute; top: 196px; left: 0; width: 1200px; text-align: center; font-weight: 700; font-size: 86px; line-height: 86px; }
  .headline-top { display: block; height: 86px; color: var(--blue); }
  .headline-top .accent { color: var(--green); }
  .headline-bottom { display: block; height: 86px; color: var(--ink); }

  .services { position: absolute; top: 466px; left: 58px; color: var(--white); }
  .services-title { font-family: "Montserrat", Arial, sans-serif; font-weight: 800; font-size: 46px; margin-bottom: 8px; }
  .services-list { list-style: none; }
  .services-item { display: flex; align-items: center; height: 55px; font-size: 31px; font-weight: 400; }
  .services-item svg { width: 40px; height: 40px; margin-right: 15px; flex: none; }

  .contact { position: absolute; left: 56px; top: 1014px; }
  .contact-phone { display: flex; align-items: center; gap: 14px; font-family: "Montserrat", Arial, sans-serif; font-weight: 800; font-size: 38px; color: var(--ink); }
  .contact-phone svg { width: 36px; height: 36px; }
  .contact-lines { display: flex; gap: 44px; margin-top: 14px; font-size: 24px; color: var(--ink); }
  .contact-line { display: flex; align-items: center; gap: 12px; }
  .contact-line svg { width: 22px; height: 22px; }
</style>
</head>
<body>
<main class="backdrop">
  <svg class="backdrop-art" viewBox="0 0 1200 1200" width="1200" height="1200">
    <defs>
      <linearGradient id="photoTones" x1="0" y1="0" x2="0" y2="1">
        <stop offset="0.22" stop-color="#8d8aa6"/>
        <stop offset="0.44" stop-color="#c7a9a4"/>
        <stop offset="0.54" stop-color="#f3c46c"/>
        <stop offset="0.6" stop-color="#9fa9bd"/>
        <stop offset="0.72" stop-color="#8fa3bb"/>
        <stop offset="0.82" stop-color="#b8a048"/>
        <stop offset="1" stop-color="#c49a2a"/>
      </linearGradient>
      <linearGradient id="blueFade" x1="0" y1="0" x2="1" y2="0">
        <stop offset="0" stop-color="#2a8cc4"/>
        <stop offset="0.38" stop-color="#2a8cc4" stop-opacity="0.95"/>
        <stop offset="0.62" stop-color="#2a8cc4" stop-opacity="0"/>
      </linearGradient>
    </defs>
    <g role="img" aria-label="Photo: woman with arms outstretched in tall golden grass overlooking the sea at sunset">
      <rect x="0" y="240" width="1200" height="960" fill="url(#photoTones)"/>
    </g>
    <rect x="0" y="240" width="1200" height="960" fill="url(#blueFade)"/>
    <path class="band-top-green" d="M0,250 C100,364 240,430 520,434 C760,440 1000,396 1200,320 V0 H0 Z" fill="var(--green)"/>
    <path class="band-top" d="M0,236 C100,350 240,415 520,419 C760,425 1000,380 1200,304 V0 H0 Z" fill="var(--white)"/>
    <path class="band-bottom-green" d="M0,910 C250,890 520,942 700,1034 C780,1080 826,1140 852,1200 H0 Z" fill="var(--green)"/>
    <path class="band-bottom" d="M0,930 C250,910 520,962 700,1052 C776,1094 818,1150 838,1200 H0 Z" fill="var(--white)"/>
  </svg>

  <header class="brand">
    <span class="brand-dot"></span>
    <span class="brand-name">MAPLE HOLLOW</span>
  </header>

  <h1 class="headline">
    <span class="headline-top">PROMOTING <span class="accent">WELLNESS</span></span>
    <span class="headline-bottom">AND RECOVERY</span>
  </h1>

  <section class="services">
    <h2 class="services-title">OUR SERVICES</h2>
    <ul class="services-list">
      <li class="services-item"><svg viewBox="0 0 40 40"><path d="M4,22 L15,33 L37,6 L15,24 Z" fill="var(--tick)"/></svg>Outpatient services</li>
      <li class="services-item"><svg viewBox="0 0 40 40"><path d="M4,22 L15,33 L37,6 L15,24 Z" fill="var(--tick)"/></svg>Treatment recovery center</li>
      <li class="services-item"><svg viewBox="0 0 40 40"><path d="M4,22 L15,33 L37,6 L15,24 Z" fill="var(--tick)"/></svg>Psychiatric services</li>
      <li class="services-item"><svg viewBox="0 0 40 40"><path d="M4,22 L15,33 L37,6 L15,24 Z" fill="var(--tick)"/></svg>Recovery housing</li>
      <li class="services-item"><svg viewBox="0 0 40 40"><path d="M4,22 L15,33 L37,6 L15,24 Z" fill="var(--tick)"/></svg>Intensive outpatient</li>
      <li class="services-item"><svg viewBox="0 0 40 40"><path d="M4,22 L15,33 L37,6 L15,24 Z" fill="var(--tick)"/></svg>Employment services</li>
    </ul>
  </section>

  <footer class="contact">
    <div class="contact-phone">
      <svg viewBox="0 0 24 24"><path d="M6.6 10.8a15.1 15.1 0 0 0 6.6 6.6l2.2-2.2a1 1 0 0 1 1-.25 11.4 11.4 0 0 0 3.6.57 1 1 0 0 1 1 1V20a1 1 0 0 1-1 1A17 17 0 0 1 3 4a1 1 0 0 1 1-1h3.5a1 1 0 0 1 1 1c0 1.25.2 2.45.57 3.57a1 1 0 0 1-.25 1z" fill="var(--green)"/></svg>
      855-555-0148
    </div>
    <div class="contact-lines">
      <span class="contact-line"><svg viewBox="0 0 24 24"><rect x="2" y="5" width="20" height="14" fill="var(--green)"/><path d="M2,5 L12,13 L22,5" fill="none" stroke="#fff" stroke-width="2"/></svg>info@maplehollow.org</span>
      <span class="contact-line"><svg viewBox="0 0 24 24"><circle cx="12" cy="12" r="9" fill="none" stroke="var(--green)" stroke-width="2"/><ellipse cx="12" cy="12" rx="4" ry="9" fill="none" stroke="var(--green)" stroke-width="2"/><path d="M3,12 H21" stroke="var(--green)" stroke-width="2"/></svg>www.maplehollow.org</span>
    </div>
  </footer>
</main>
</body>
</html>
```